BUSINESS CARD needed for TRAVEL BUSINESS

-Background-

Roamvista Crew (RC) is a newly found company in Asia that trains and develops people with various demographics to become a FREQUENT TRAVELER & an ENTREPRENEUR combined. Basically, the core product that the company markets teaches people how to TRAVEL leisurely and yet EARN MONEY at the same time. Our main quote will be LIVING LIFE BY LIVING.

- The Job -

We will be constantly going out to different events, whether opening promotional booths in roadshows or at colleges or going for networking events. Thus we need a BUSINESS CARD design that portrays our POSITIONING & BRANDING

- Positioning -

TRAVEL LEISURELY & EARN at the SAME TIME

- Objective -

Serve as a BTL marketing & networking tool

- Target Audience -

Male & Females aged 19 - 35 who LOVES to TRAVEL & have strong aspirations to make it big and attaining financial freedom. The audience are enthusiastic and when they see an opportunity, they will seize it on the very spot. They are well connected and have a wide social network.

- Single Minded Proposition -

RC is My Dream Life

Target Market(s)

REFER TO CREATIVE BRIEF

Industry/Entity Type

Marketing

Requirements
Must have
• 1) The business card must portray a branding thats related to TRAVEL.

Boarding pass design was what we came up with but express your creativity and surprise me with better ideas. :)
Nice to have
• This is an idea that we have and we would most likely like to use however I do not want to restrict your creativity so i am putting in NICE TO HAVE instead.

Our idea design -> To have the namecard in the format of a BOARDING PASS lookalike

(You may refer to these weblink for inspiration -> https://www.findlopix.example/search?hl=en&q=boarding+pass&bav=on.2,or.r_gc.r_pw.r_cp.r_qf.,cf.osb&biw=1366&bih=667&um=1&ie=UTF-8&tbm=isch&source=og&sa=N&tab=wi&ei=l-f9T4KqC4fWrQfx8eC-Bg

or simply FINDLOPIX BOARDING PASS IMAGES

```html
<!DOCTYPE html>
<html lang="en">
<head>
<meta charset="utf-8">
<title>Roamvista Crew – Business Card</title>
<link rel="stylesheet" href="https://fonts.googleapis.com/css2?family=Arimo:wght@400;700&display=swap">
<style>
  :root {
    --page-bg: #e8e3dc;
    --ticket-orange: #ff7a00;
    --ticket-paper: #ffffff;
    --stripe: #f3f0e4;
    --ink: #111111;
    --ink-muted: #9a9a9a;
    --ink-white: #ffffff;
    --address-fill: #ecd2bb;
    --address-edge: #d9bfa7;
  }
  * { box-sizing: border-box; margin: 0; padding: 0; }
  html, body {
    width: 1200px; height: 968px; overflow: hidden;
    background: var(--page-bg);
    font-family: "Arimo", Arial, sans-serif;
  }
  .business-card {
    position: absolute; left: 100px; top: 144px;
    width: 1000px; height: 680px;
    border-radius: 22px; overflow: hidden;
    background: repeating-linear-gradient(to bottom, var(--ticket-paper) 0 14px, var(--stripe) 14px 16px);
    box-shadow: 0 6px 18px rgba(0,0,0,.18);
    color: var(--ink);
  }
  .business-card p, .business-card h1, .business-card h2 { line-height: 1.1; white-space: nowrap; }
  .card-header {
    position: absolute; left: 0; top: 0; width: 100%; height: 92px;
    background: var(--ticket-orange);
  }
  .validity { position: absolute; left: 18px; top: 28px; font-size: 36px; }
  .coupons {
    position: absolute; left: 730px; top: 30px;
    font-size: 20px; line-height: 1.15;
  }
  .coupons span { display: block; }
  .coupons .count { padding-left: 6px; }
  .monogram {
    position: absolute; right: 22px; top: 8px;
    font-size: 78px; font-weight: 700; letter-spacing: 1px;
  }
  .field-label { position: absolute; font-size: 22px; color: var(--ink-muted); }
  .field-value { position: absolute; color: var(--ink-muted); }
  .class-label { left: 20px; top: 112px; }
  .class-value { left: 20px; top: 136px; font-size: 56px; font-weight: 700; }
  .type-label { left: 170px; top: 112px; }
  .type-value { left: 170px; top: 144px; font-size: 36px; }
  .adult-label { left: 560px; top: 148px; font-size: 26px; }
  .adult-value { left: 560px; top: 178px; font-size: 38px; }
  .senior { left: 20px; top: 234px; font-size: 46px; font-weight: 700; }
  .travelling { left: 170px; top: 236px; font-size: 40px; }
  .company {
    position: absolute; left: 470px; top: 244px;
    font-size: 52px; font-weight: 700; text-decoration: underline;
    text-decoration-thickness: 4px; text-underline-offset: 6px;
  }
  .address-label { position: absolute; left: 520px; top: 320px; font-size: 24px; font-weight: 700; }
  .address-box {
    position: absolute; left: 640px; top: 352px; width: 330px; height: 176px;
    background: var(--address-fill); border: 2px solid var(--address-edge);
  }
  .from-label { left: 20px; top: 330px; }
  .to-label { left: 20px; top: 408px; }
  .holder-name {
    position: absolute; left: 176px; top: 446px;
    font-size: 64px; font-weight: 700;
  }
  .card-footer {
    position: absolute; left: 0; top: 530px; width: 100%; height: 150px;
    background: var(--ticket-orange);
  }
  .issuer {
    position: absolute; left: 28px; top: 44px;
    font-size: 30px; font-weight: 700; color: var(--ink-white);
  }
  .tel-label { position: absolute; left: 160px; top: 44px; font-size: 32px; font-weight: 700; }
  .tel-number { position: absolute; left: 262px; top: 46px; font-size: 32px; font-weight: 700; letter-spacing: 1px; }
  .fare-type { position: absolute; left: 690px; top: 26px; font-size: 58px; font-weight: 700; }
  .printed-note { position: absolute; left: 580px; top: 112px; font-size: 22px; font-weight: 700; }
</style>
</head>
<body>
  <article class="business-card">
    <header class="card-header">
      <p class="validity">VALID ONLY WITH RESERVATIONS</p>
      <p class="coupons"><span>ISSUED AS</span><span class="count">2&nbsp; COUPONS</span></p>
      <p class="monogram">RC</p>
    </header>

    <p class="field-label class-label">Class</p>
    <p class="field-value class-value">1ST</p>
    <p class="field-label type-label">Ticket Type</p>
    <p class="field-value type-value">ADVANCED 1ST</p>
    <p class="field-label adult-label">Adult</p>
    <p class="field-value adult-value">ONE</p>

    <p class="field-value senior">SNR</p>
    <p class="field-value travelling">Travelling with</p>
    <h1 class="company">Roamvista Crew</h1>

    <p class="address-label">Address</p>
    <div class="address-box"></div>

    <p class="field-label from-label">From</p>
    <p class="field-label to-label">To</p>
    <h2 class="holder-name">Mara Quinlan</h2>

    <footer class="card-footer">
      <p class="issuer">Raylane</p>
      <p class="tel-label">Tel</p>
      <p class="tel-number">0123456789</p>
      <p class="fare-type">SINGLE</p>
      <p class="printed-note">Printed for the traveller</p>
    </footer>
  </article>
</body>
</html>
```